Brenway Productions photography and video creator

I need a business card for my production company. I shoot photography and videography for real estate, adventure sports and businesses

simple not to busy

Colors

Designer to choose colors to be used in the design.

Requirements
Must have
• dara@brenwayproductions.ca
• phone -5803317264
• instagram dara_brenway

```html
<!DOCTYPE html>
<html lang="en">
<head>
<meta charset="utf-8">
<title>Brenway Productions — Business Card</title>
<link rel="stylesheet" href="https://fonts.googleapis.com/css2?family=Montserrat:wght@600;700&family=Source+Sans+3:wght@400&display=swap">
<style>
  :root {
    --page: #e2e2e2;
    --card-dark: #1e1e1e;
    --ink-white: #ffffff;
    --mist: #f2f2f2;
    --ridge-light: #cfcfcf;
    --ridge-mid: #8a8a8a;
    --ridge-dark: #3a3a3a;
    --ground: #141414;
  }
  html, body {
    margin: 0;
    padding: 0;
    width: 1200px;
    height: 1200px;
    overflow: hidden;
    background: var(--page);
  }
  .canvas {
    position: relative;
    width: 1200px;
    height: 1200px;
    background: var(--page);
  }
  .card {
    position: absolute;
    left: 220px;
    width: 759px;
    height: 434px;
    overflow: hidden;
  }
  .card--front { top: 109px; background: var(--card-dark); }
  .card--back  { top: 651px; background: var(--card-dark); }

  .landscape-backdrop {
    position: absolute;
    inset: 0;
    background: linear-gradient(180deg,
      var(--mist) 0%,
      var(--ridge-light) 22%,
      var(--ridge-mid) 45%,
      var(--ridge-dark) 62%,
      var(--ground) 80%,
      var(--card-dark) 100%);
  }
  .emblem {
    position: absolute;
    border-radius: 50%;
    overflow: hidden;
  }
  .card--front .emblem {
    left: 227px; top: 57px;
    width: 320px; height: 320px;
    background: linear-gradient(180deg,
      var(--mist) 0%,
      var(--ridge-light) 18%,
      var(--ridge-mid) 34%,
      var(--ridge-dark) 48%,
      var(--ground) 62%,
      #080808 100%);
  }
  .card--back .emblem {
    left: 259px; top: 94px;
    width: 242px; height: 242px;
    background: linear-gradient(180deg,
      var(--mist) 0%,
      var(--ridge-light) 20%,
      var(--ridge-mid) 35%,
      var(--ridge-dark) 48%,
      var(--card-dark) 56%,
      var(--card-dark) 78%,
      #080808 100%);
  }
  .wordmark {
    position: absolute;
    left: 0; right: 0;
    text-align: center;
    color: var(--ink-white);
    font-family: "Montserrat", sans-serif;
    font-weight: 700;
    line-height: 1;
  }
  .wordmark__name { display: block; }
  .wordmark__sub  { display: block; }

  .card--front .wordmark { top: 252px; }
  .card--front .wordmark__name { font-size: 46px; letter-spacing: 0.5px; }
  .card--front .wordmark__sub  { font-size: 12px; letter-spacing: 8px; margin-top: 10px; padding-left: 8px; }

  .card--back .wordmark { top: 246px; }
  .card--back .wordmark__name { font-size: 35px; letter-spacing: 0.5px; }
  .card--back .wordmark__sub  { font-size: 9px; letter-spacing: 6px; margin-top: 8px; padding-left: 6px; }

  .contact {
    position: absolute;
    display: flex;
    align-items: center;
    color: var(--ink-white);
  }
  .contact svg { flex: none; }
  .contact--phone { left: 30px; top: 352px; }
  .contact--phone .contact__text {
    font-family: "Montserrat", sans-serif;
    font-weight: 700;
    font-size: 20px;
    margin-left: 20px;
  }
  .contact--email { left: 30px; top: 388px; }
  .contact--email .contact__text,
  .contact--social .contact__text {
    font-family: "Source Sans 3", sans-serif;
    font-weight: 400;
    font-size: 19px;
  }
  .contact--email .contact__text { margin-left: 17px; }
  .contact--social { right: 27px; top: 385px; }
  .contact--social .contact__text { margin-left: 17px; }
  .social-mark {
    width: 24px; height: 24px;
    border: 2.5px solid var(--ink-white);
    border-radius: 6px;
    box-sizing: border-box;
  }
</style>
</head>
<body>
<main class="canvas">

  <section class="card card--front" aria-label="Card front">
    <div class="landscape-backdrop" role="img" aria-label="Soft-focus greyscale mountain ridges with pine trees"></div>
    <div class="emblem" role="img" aria-label="Circular greyscale mountain landscape with pine trees"></div>
    <div class="wordmark">
      <span class="wordmark__name">BRENWAY</span>
      <span class="wordmark__sub">PRODUCTIONS</span>
    </div>

    <div class="contact contact--phone">
      <svg width="26" height="26" viewBox="0 0 24 24" aria-hidden="true">
        <path d="M6.6 2.5 4.3 4.2c-1 .8-1.2 2.2-.7 3.4 2.3 5.6 6.8 10.1 12.4 12.6 1.2.5 2.6.2 3.4-.8l1.6-2.2-4-2.8-1.8 1.7c-2.8-1.4-5.2-3.8-6.6-6.6l1.7-1.8Z" fill="none" stroke="#fff" stroke-width="1.6" stroke-linejoin="round"/>
        <path d="M14 3.5a6.5 6.5 0 0 1 6.5 6.5M14 6.5a3.5 3.5 0 0 1 3.5 3.5" fill="none" stroke="#fff" stroke-width="1.4" stroke-linecap="round"/>
      </svg>
      <span class="contact__text">5803317264</span>
    </div>

    <div class="contact contact--email">
      <svg width="30" height="20" viewBox="0 0 30 20" aria-hidden="true">
        <rect x="0" y="0" width="30" height="20" fill="#fff"/>
        <path d="M1 1 15 12 29 1M1 19 11 9M29 19 19 9" fill="none" stroke="#1e1e1e" stroke-width="1.6"/>
      </svg>
      <span class="contact__text">dara@brenwayproductions.ca</span>
    </div>

    <div class="contact contact--social">
      <span class="social-mark" aria-hidden="true"></span>
      <span class="contact__text">dara_brenway</span>
    </div>
  </section>

  <section class="card card--back" aria-label="Card back">
    <div class="emblem" role="img" aria-label="Circular greyscale mountain landscape with pine trees"></div>
    <div class="wordmark">
      <span class="wordmark__name">BRENWAY</span>
      <span class="wordmark__sub">PRODUCTIONS</span>
    </div>
  </section>

</main>
</body>
</html>
```